Banner design for an online shop

We need a banner for our online shop www.velmora-shop.de
This should be displayed on the start page in the carousel.
The banner should have the following dimensions: 1420 x 424 px

```html
<!DOCTYPE html>
<html lang="de">
<head>
<meta charset="utf-8">
<title>Mobiler Strom – Stromerzeuger</title>
<link href="https://fonts.googleapis.com/css2?family=Open+Sans:wght@300;600;700;800&display=swap" rel="stylesheet">
<style>
  :root {
    --sky-deep: #5c9fc6;
    --sky-mid: #80b8d6;
    --sky-light: #b7d8ea;
    --glow: #eef6fb;
    --navy: #1f3b6e;
    --headline-top: #5d8fc4;
    --headline-bottom: #1c3566;
    --white: #ffffff;
    --side-text: rgba(120, 176, 210, 0.75);
    --product-blue: #2c4fa8;
    --product-dark: #1b1d22;
  }
  html, body {
    margin: 0;
    padding: 0;
    width: 1200px;
    height: 358px;
    overflow: hidden;
  }
  .banner {
    position: relative;
    width: 1200px;
    height: 358px;
    overflow: hidden;
    font-family: "Open Sans", sans-serif;
    background: linear-gradient(90deg, var(--sky-deep) 0%, var(--sky-mid) 45%, var(--sky-light) 100%);
  }
  .banner__glow {
    position: absolute;
    left: 560px;
    top: -60px;
    width: 560px;
    height: 480px;
    background: radial-gradient(ellipse at center, var(--glow) 0%, rgba(238,246,251,0.6) 35%, rgba(238,246,251,0) 70%);
  }
  .headline {
    position: absolute;
    left: 80px;
    top: 80px;
    margin: 0;
    font-weight: 800;
    font-size: 51px;
    line-height: 1;
    letter-spacing: 0.5px;
    background: linear-gradient(180deg, var(--headline-top) 0%, var(--headline-bottom) 90%);
    -webkit-background-clip: text;
    background-clip: text;
    color: transparent;
    -webkit-text-stroke: 2px var(--white);
    filter: drop-shadow(0 2px 3px rgba(20, 40, 80, 0.45));
  }
  .subline {
    position: absolute;
    left: 82px;
    top: 160px;
    margin: 0;
    font-weight: 300;
    font-size: 47px;
    line-height: 1;
    color: var(--white);
    letter-spacing: 0.3px;
  }
  .cta {
    position: absolute;
    left: 93px;
    top: 243px;
    width: 183px;
    height: 54px;
    border-radius: 27px;
    background: var(--navy);
    color: var(--white);
    text-decoration: none;
    display: flex;
    align-items: center;
  }
  .cta__label {
    margin-left: 28px;
    font-weight: 700;
    font-size: 13px;
    letter-spacing: 0.2px;
  }
  .cta__icon {
    position: absolute;
    right: 7px;
    top: 5px;
    width: 44px;
    height: 44px;
    border-radius: 50%;
    background: var(--white);
    display: flex;
    align-items: center;
    justify-content: center;
  }
  .product {
    position: absolute;
    left: 640px;
    top: 68px;
    width: 370px;
    height: 266px;
    border-radius: 14px;
    background: linear-gradient(160deg, var(--product-dark) 0%, var(--product-blue) 40%, #3b5fb8 70%, var(--product-dark) 100%);
    opacity: 0.9;
  }
  .side-word {
    position: absolute;
    top: 98px;
    height: 180px;
    margin: 0;
    writing-mode: vertical-rl;
    transform: rotate(180deg);
    text-align: center;
    font-weight: 700;
    font-size: 44px;
    line-height: 1;
    color: var(--side-text);
  }
  .side-word--first { left: 1064px; }
  .side-word--second { left: 1113px; }
</style>
</head>
<body>
  <div class="banner">
    <div class="banner__glow"></div>

    <h1 class="headline">MOBILER STROM</h1>
    <p class="subline">STROMERZEUGER</p>

    <a class="cta" href="#">
      <span class="cta__label">MEHR INFOS</span>
      <span class="cta__icon">
        <svg width="14" height="12" viewBox="0 0 14 12" aria-hidden="true">
          <path d="M2 1 L7 6 L2 11 M7 1 L12 6 L7 11" fill="none" stroke="#1f3b6e" stroke-width="1.8" stroke-linecap="round" stroke-linejoin="round"/>
        </svg>
      </span>
    </a>

    <div class="product" role="img" aria-label="Produktfoto: blauer tragbarer Stromerzeuger mit schwarzem Rohrrahmen und Steckdosen"></div>

    <p class="side-word side-word--first">MOBILER</p>
    <p class="side-word side-word--second">STROM</p>
  </div>
</body>
</html>
```